Website Needs Designing / Populating

We are a Business Consultancy in London. We are Headhunters and Recruitment. I have bought the Domain, and Wordpress Site, installed a template from Pagecraft Yard. I have tried to do it myself but do not have the time to complete or do it as I want / need.
I have some 'stock' pics and a logo - see uploaded logo files.
I want an easy to use Website - tells clients and viewers what we are about.
We are a recruitment / Headhunting Consultancy so some visitors may want to apply for positions through loading their CV / Details through the site.
We want to be about friendly but expertise. Honest and trustworthy with a heavy emphasis on Consultancy!

Target Market(s)

Northgate Talent Job Seekers. Our clients are in the Marketing Communications sectors so needs to be appealing to that market

Industry/Entity Type

Business Consultant

Number of Pages Required

3 page

Requirements
Must have
• Our Logo as a central theme - see uploaded files
Nice to have
• Simple. Easy to use, inviting

```html
<!DOCTYPE html>
<html lang="en">
<head>
<meta charset="utf-8">
<title>Northgate Talent — Recruitment</title>
<link rel="stylesheet" href="https://fonts.googleapis.com/css2?family=Raleway:wght@300;400;600;700&family=Open+Sans:wght@400;600;700&display=swap">
<style>
:root{
  --blue:#0a9fe0;
  --teal:#17b3c4;
  --yellow:#fcc514;
  --purple:#6d2c8e;
  --dark:#3b3b3b;
  --darker:#2a2a2a;
  --ink:#444;
  --muted:#9a9a9a;
  --white:#fff;
}
*{margin:0;padding:0;box-sizing:border-box}
html,body{width:1200px;height:3169px;overflow:hidden}
body{position:relative;font-family:"Open Sans",Arial,sans-serif;color:var(--ink);background:var(--white)}
.abs{position:absolute}
a{color:inherit;text-decoration:none}

/* top bar */
.topbar{left:0;top:0;width:1200px;height:44px;background:var(--dark);color:#eee;font-size:12px}
.topbar .info{top:0;height:44px;display:flex;align-items:center;gap:8px}
.topbar svg{width:14px;height:14px}
.btn-register,.btn-login{top:0;height:44px;display:flex;align-items:center;justify-content:center;font-size:12px;font-weight:600;color:#fff}
.btn-register{left:883px;width:134px;background:var(--teal)}
.btn-login{left:1017px;width:103px;background:var(--blue)}

/* header */
.header{left:0;top:44px;width:1200px;height:100px;background:#fff;box-shadow:0 1px 3px rgba(0,0,0,.08)}
.brand{left:84px;top:16px;display:flex;flex-direction:column}
.brand-name{font-family:"Raleway",sans-serif;font-weight:700;font-size:38px;color:var(--dark);line-height:1}
.brand-sub{font-family:"Raleway",sans-serif;font-weight:700;font-size:13px;letter-spacing:9px;color:var(--dark);margin-top:6px}
.nav{left:471px;top:0;height:100px;display:flex}
.nav a{height:100px;display:flex;align-items:center;justify-content:center;font-size:12px;font-weight:600;color:#333;padding:0 24px}
.nav a.active{background:var(--blue);color:#fff;width:93px;flex-direction:column;gap:6px}

/* hero */
.hero{left:0;top:144px;width:1200px;height:536px;background:linear-gradient(120deg,#4a4038 0%,#7b6a5c 35%,#9b8b7e 55%,#5a4e46 80%,#3a332e 100%)}
.hero-title{left:0;top:320px;width:1200px;text-align:center;font-family:"Raleway",sans-serif;font-size:48px;font-weight:400;color:#fff}
.hero-title b{color:var(--yellow);font-weight:600}
.hero-text{left:0;top:390px;width:1200px;text-align:center;font-size:18px;line-height:24px;color:#fff}
.btn-hero{left:492px;top:465px;width:216px;height:46px;border-radius:23px;background:var(--blue);color:#fff;font-size:14px;display:flex;align-items:center;justify-content:center}

/* sections */
.sec-title{left:0;width:1200px;text-align:center;font-family:"Raleway",sans-serif;font-size:32px;font-weight:300;color:#888;letter-spacing:1px}
.sec-title b{font-weight:700;color:#555}
.sec-sub{left:0;width:1200px;text-align:center;font-size:13px;color:var(--muted)}

.service{width:300px;text-align:center}
.service .ring{width:156px;height:156px;border-radius:50%;border:3px solid #ddd;margin:0 auto;display:flex;align-items:center;justify-content:center}
.service .disc{width:142px;height:142px;border-radius:50%;display:flex;align-items:center;justify-content:center}
.service h3{font-family:"Raleway",sans-serif;font-size:21px;font-weight:600;color:#333;margin-top:50px}
.service p{font-size:13px;line-height:24px;color:var(--muted);margin-top:16px}
.btn-pill{display:flex;align-items:center;justify-content:center;width:188px;height:40px;border-radius:20px;color:#fff;font-size:11px;font-weight:600;margin:30px auto 0}

/* who we are */
.about{left:0;top:1352px;width:1200px;height:571px;background:linear-gradient(90deg,#1f1f1f,#2d2d2d 60%,#3a3a3a)}
.about .sec-title{color:#ddd}
.about .sec-title b{color:#fff}
.about .sec-sub{color:#aaa}
.device{left:144px;top:1547px;width:469px;height:287px;border-radius:8px;background:linear-gradient(135deg,#5a6a7a,#8aa0b0 50%,#3c4650)}
.about-text{left:661px;top:1570px;width:450px;color:#fff;font-size:17px;line-height:24px}
.about-mission{left:661px;top:1692px;width:450px;color:#ddd;font-size:14px;line-height:25px}

/* news */
.news-card{top:2100px;width:229px}
.news-img{width:229px;height:165px;border:1px solid #ccc}
.news-card p{font-size:14px;line-height:21px;color:#333;margin-top:14px}
.news-date{display:flex;align-items:center;gap:8px;font-size:11px;color:#777;margin-top:10px}

/* cta */
.cta{left:0;top:2426px;width:1200px;height:384px;background:linear-gradient(120deg,#4d5258,#7a7e82 50%,#5b5f63)}
.cta-line1{left:133px;top:2505px;font-family:"Raleway",sans-serif;font-size:30px;color:#fff;letter-spacing:.5px}
.cta-line2{left:133px;top:2541px;font-family:"Raleway",sans-serif;font-size:22px;font-weight:700;color:#fff}
.btn-cta{left:858px;top:2521px;width:211px;height:46px;border-radius:23px;background:var(--yellow);color:#333;font-size:13px;font-weight:700}

/* footer */
.footer{left:0;top:2810px;width:1200px;height:313px;background:var(--blue)}
.newsletter{left:95px;top:2643px;width:1012px;height:216px;background:var(--yellow);text-align:center}
.newsletter h2{font-family:"Raleway",sans-serif;font-size:30px;font-weight:700;color:#333;margin-top:42px;letter-spacing:1px}
.newsletter p{font-size:13px;color:#fff;margin-top:4px}
.nl-form{display:flex;justify-content:center;gap:22px;margin-top:22px}
.nl-input{width:370px;height:40px;border-radius:20px;background:#fff;display:flex;align-items:center;justify-content:space-between;padding:0 20px;font-size:12px;color:#888}
.nl-btn{width:132px;height:40px;border-radius:20px;background:#3a3a3a;color:#fff;font-size:12px;font-weight:700;display:flex;align-items:center;justify-content:center}

.foot-brand{left:124px;top:2915px}
.foot-brand .brand-name,.foot-brand .brand-sub{color:#fff}
.socials{left:158px;top:3024px;display:flex;gap:22px}
.socials span{width:14px;height:14px;border-radius:50%;background:var(--yellow)}
.foot-col{top:2918px}
.foot-col h4{font-family:"Raleway",sans-serif;font-size:17px;font-weight:600;color:var(--yellow);margin-bottom:20px}
.foot-col li{list-style:none;font-size:12px;color:#fff;line-height:25px}
.contact-line{display:flex;align-items:center;gap:14px;font-size:13px;color:#fff;line-height:30px}
.copyright{left:0;top:3123px;width:1200px;height:46px;background:#3a3a3a;color:#888;font-size:11px;display:flex;align-items:center;justify-content:center}
.copyright b{color:var(--yellow);font-weight:600;margin:0 4px}
</style>
</head>
<body>

<!-- top bar -->
<div class="abs topbar">
  <div class="abs info" style="left:84px">
    <svg viewBox="0 0 24 24"><path fill="#fcc514" d="M12 2a7 7 0 0 0-7 7c0 5 7 13 7 13s7-8 7-13a7 7 0 0 0-7-7zm0 9.5A2.5 2.5 0 1 1 12 6.5a2.5 2.5 0 0 1 0 5z"/></svg>
    <span>48 Larkspur Row, London EC2 4QT UK.</span>
  </div>
  <div class="abs info" style="left:440px">
    <svg viewBox="0 0 24 24"><circle cx="12" cy="12" r="9" fill="none" stroke="#17b3c4" stroke-width="2"/><path d="M12 7v5l3 2" fill="none" stroke="#17b3c4" stroke-width="2"/></svg>
    <span>Mon - Sat 8.00 - 18.00. Sunday CLOSED</span>
  </div>
  <div class="abs info" style="left:737px">
    <svg viewBox="0 0 24 24"><path fill="#0a9fe0" d="M6.6 10.8a15 15 0 0 0 6.6 6.6l2.2-2.2a1 1 0 0 1 1-.25 11 11 0 0 0 3.6.6 1 1 0 0 1 1 1V20a1 1 0 0 1-1 1A17 17 0 0 1 3 4a1 1 0 0 1 1-1h3.5a1 1 0 0 1 1 1 11 11 0 0 0 .6 3.6 1 1 0 0 1-.25 1z"/></svg>
    <span>020 555 0142</span>
  </div>
  <a class="abs btn-register" href="#">REGISTER</a>
  <a class="abs btn-login" href="#">LOGIN</a>
</div>

<!-- header -->
<header class="abs header">
  <div class="abs brand">
    <span class="brand-name">northgate</span>
    <span class="brand-sub">Recruitment</span>
  </div>
  <nav class="abs nav">
    <a class="active" href="#"><svg width="12" height="12" viewBox="0 0 12 12"><path d="M1 1l10 5-10 5z" fill="#fff"/></svg>HOME</a>
    <a href="#">ABOUT US</a>
    <a href="#">SERVICES</a>
    <a href="#">BLOG</a>
    <a href="#">TEAM</a>
    <a href="#">CONTACT US</a>
  </nav>
</header>

<!-- hero -->
<section class="abs hero" role="img" aria-label="Photo of a business team meeting around a table with laptops"></section>
<h1 class="abs hero-title">WELCOME TO <b>NORTHGATE TALENT</b></h1>
<p class="abs hero-text">Lorem ipsum dolor sit amet, consectetur adipiscing elit. In convallis augue,<br>porta vitae. Mauris arcu lectus, accumsan vitae posuere quam.</p>
<a class="abs btn-hero" href="#">Sign up for an account</a>

<!-- services -->
<h2 class="abs sec-title" style="top:734px">OUR <b>SERVICES</b></h2>
<p class="abs sec-sub" style="top:790px">Donec cursus ornare ipsum. Vestibulum dapibus vitae ante id finibus Nulla ultrices suscipit.</p>

<div class="abs service" style="left:82px;top:875px">
  <div class="ring"><div class="disc" style="background:var(--purple)">
    <svg width="64" height="64" viewBox="0 0 64 64" fill="none" stroke="#fff" stroke-width="4"><path d="M52 32a20 20 0 1 1-6-14"/><path d="M46 10v8h-8"/><path d="M24 42l16-20"/><circle cx="25" cy="24" r="4"/><circle cx="39" cy="40" r="4"/></svg>
  </div></div>
  <h3>Consultancy</h3>
  <p>Lorem ipsum dolor sit amet, consectetur adipiscing elit. Mauris sed elementum arcu. Donec cursus ornare ipsum.</p>
  <a class="btn-pill" style="background:var(--purple)" href="#">READ MORE</a>
</div>

<div class="abs service" style="left:448px;top:875px">
  <div class="ring"><div class="disc" style="background:var(--yellow)">
    <svg width="66" height="60" viewBox="0 0 66 60" fill="none" stroke="#fff" stroke-width="4"><rect x="4" y="16" width="58" height="38" rx="5"/><path d="M24 16V9h18v7"/><path d="M4 30h58"/><rect x="28" y="26" width="10" height="8" fill="#fff"/></svg>
  </div></div>
  <h3>Headhunters</h3>
  <p>Lorem ipsum dolor sit amet, consectetur adipiscing elit. Mauris sed elementum arcu. Donec cursus ornare ipsum.</p>
  <a class="btn-pill" style="background:var(--yellow)" href="#">READ MORE</a>
</div>

<div class="abs service" style="left:811px;top:875px">
  <div class="ring"><div class="disc" style="background:var(--blue)">
    <svg width="60" height="64" viewBox="0 0 60 64" fill="none" stroke="#fff" stroke-width="4"><circle cx="30" cy="20" r="13"/><path d="M6 60c0-14 10-22 24-22s24 8 24 22z"/><path d="M26 38l4 10 4-10"/></svg>
  </div></div>
  <h3>Recruitment</h3>
  <p>Lorem ipsum dolor sit amet, consectetur adipiscing elit. Mauris sed elementum arcu. Donec cursus ornare ipsum.</p>
  <a class="btn-pill" style="background:var(--blue)" href="#">READ MORE</a>
</div>

<!-- who we are -->
<section class="abs about" role="img" aria-label="Dark background photo of a keyboard on a desk"></section>
<h2 class="abs sec-title" style="top:1408px;color:#ddd">WHO <b style="color:#fff">WE ARE</b></h2>
<p class="abs sec-sub" style="top:1472px;color:#aaa">Donec cursus ornare ipsum. Vestibulum dapibus vitae ante id finibus Nulla ultrices suscipit.</p>
<div class="abs device" role="img" aria-label="Laptop displaying the Northgate Talent home page"></div>
<p class="abs about-text">Northgate Talent Solutions is an information-technology consulting and services company that provides custom solutions based on JEETM, Web Services, and related technologies.</p>
<p class="abs about-mission">Our mission is to help organizations successfully create and deploy custom software applications using emerging technologies.</p>
<a class="abs btn-pill" style="left:666px;top:1751px;background:var(--yellow);color:#333" href="#">READ MORE</a>

<!-- news -->
<h2 class="abs sec-title" style="top:1975px">LATEST <b>NEWS</b></h2>
<p class="abs sec-sub" style="top:2030px">Donec cursus ornare ipsum. Vestibulum dapibus vitae ante id finibus Nulla ultrices suscipit.</p>

<article class="abs news-card" style="left:106px">
  <div class="news-img" role="img" aria-label="Photo of business people shaking hands" style="background:linear-gradient(135deg,#dfe3e6,#8c939a)"></div>
  <p>Lorem ipsum dolor sit amet cons ectetur adipiscing elit.</p>
  <div class="news-date"><svg width="14" height="14" viewBox="0 0 24 24"><circle cx="12" cy="12" r="9" fill="none" stroke="#fcc514" stroke-width="3"/><path d="M12 7v5l3 2" fill="none" stroke="#fcc514" stroke-width="3"/></svg>January 23, 2016</div>
</article>
<article class="abs news-card" style="left:360px">
  <div class="news-img" role="img" aria-label="Photo of a man working at a desk with a laptop" style="background:linear-gradient(135deg,#f1efea,#a9a39a)"></div>
  <p>Lorem ipsum dolor sit amet cons ectetur adipiscing elit.</p>
  <div class="news-date"><svg width="14" height="14" viewBox="0 0 24 24"><circle cx="12" cy="12" r="9" fill="none" stroke="#fcc514" stroke-width="3"/><path d="M12 7v5l3 2" fill="none" stroke="#fcc514" stroke-width="3"/></svg>January 23, 2016</div>
</article>
<article class="abs news-card" style="left:614px">
  <div class="news-img" role="img" aria-label="Photo of a businessman reviewing documents" style="background:linear-gradient(135deg,#3a4250,#6c7480)"></div>
  <p>Lorem ipsum dolor sit amet cons ectetur adipiscing elit.</p>
  <div class="news-date"><svg width="14" height="14" viewBox="0 0 24 24"><circle cx="12" cy="12" r="9" fill="none" stroke="#fcc514" stroke-width="3"/><path d="M12 7v5l3 2" fill="none" stroke="#fcc514" stroke-width="3"/></svg>January 23, 2016</div>
</article>
<article class="abs news-card" style="left:869px">
  <div class="news-img" role="img" aria-label="Photo of a businesswoman holding a folder" style="background:linear-gradient(135deg,#f5f5f5,#b9b4ae)"></div>
  <p>Lorem ipsum dolor sit amet cons ectetur adipiscing elit.</p>
  <div class="news-date"><svg width="14" height="14" viewBox="0 0 24 24"><circle cx="12" cy="12" r="9" fill="none" stroke="#fcc514" stroke-width="3"/><path d="M12 7v5l3 2" fill="none" stroke="#fcc514" stroke-width="3"/></svg>January 23, 2016</div>
</article>

<!-- call to action -->
<section class="abs cta" role="img" aria-label="Photo of hands using a tablet beside a coffee cup"></section>
<p class="abs cta-line1">WE ADVISE INVENTORS AND TECHNOLOGY</p>
<p class="abs cta-line2">EXPERTS AND HELP THEM BRING NEW PRODUCTS TO MARKET.</p>
<a class="abs btn-cta btn-pill" style="margin:0" href="#">GET ADVICES</a>

<!-- footer -->
<footer class="abs footer"></footer>
<div class="abs newsletter">
  <h2>NEWSLETTER</h2>
  <p>Enter Your Email address for getting Updates</p>
  <div class="nl-form">
    <div class="nl-input"><span>Enter Your Email Address</span>
      <svg width="16" height="12" viewBox="0 0 16 12" fill="none" stroke="#999" stroke-width="1.5"><rect x="1" y="1" width="14" height="10"/><path d="M1 1l7 6 7-6"/></svg></div>
    <div class="nl-btn">SUBSCRIBE</div>
  </div>
</div>

<div class="abs brand foot-brand">
  <span class="brand-name">northgate</span>
  <span class="brand-sub">Recruitment</span>
</div>
<div class="abs socials"><span></span><span></span><span></span><span></span><span></span></div>

<div class="abs foot-col" style="left:475px">
  <h4>MAIN MENU</h4>
  <ul><li>Home</li><li>What We Do</li><li>Consulting</li><li>Contact</li></ul>
</div>
<div class="abs foot-col" style="left:702px">
  <h4>QUICK LINKS</h4>
  <ul><li>Get Quote</li><li>Our Law Team</li><li>About Us</li><li>FAQ</li></ul>
</div>
<div class="abs foot-col" style="left:928px">
  <h4>CONTACT US</h4>
  <div class="contact-line"><svg width="12" height="18" viewBox="0 0 12 18"><rect x="1" y="1" width="10" height="16" rx="2" fill="none" stroke="#fcc514" stroke-width="2"/><circle cx="6" cy="14" r="1" fill="#fcc514"/></svg>020-555-0187</div>
  <div class="contact-line"><svg width="16" height="12" viewBox="0 0 16 12"><rect width="16" height="12" rx="1" fill="#fcc514"/><path d="M0 0l8 6 8-6" fill="none" stroke="#0a9fe0" stroke-width="1.5"/></svg>hello@northgatetalent.example</div>
</div>

<div class="abs copyright">© 2016 <b>Northgate Talent</b> All Rights Reserved</div>

</body>
</html>
```